Business Card Design for Massage Therapist

*I am a qualified massage therapist & require a business card for my new business 'Tidal Touch & Wellness'.
*Contact details I'd like included on the card are: Elise Brantry, Mobile: 0481562930, Email: tidaltw@mailvane.com
*It is a massage business dedicated to providing quality therapeutic massage treatments, that will later incorporate natural therapies.
* Styles Include: Swedish, Relaxation, Pregnancy, Deep Tissue & Sports Massage
*I offer the styles of massage as listed above & a mobile service that allows clients to book a massage in the comfort of their own home.
*I'd like my logo to be fairly simple, streamlined, modern & reflect what my business services are - one people will easily remember.
*I'd like the colors to represent & emit a sense of calm, be fresh, welcoming, natural colors that appeal to a wide range of people.
*Colors I'd like to see are: pale blue, aqua & greens.

Target Market(s)

Both Male & Female, aged 20 to 65, singles, couples, parents, business people who are interested in their health, fitness & general wellbeing and maintenance. Located in the Harbourvale area and surrounding suburbs of Melbourne.

Industry/Entity Type

Massage

Requirements
Must have
• Fonts used in logos should be owned by the designer.
Should not have
• I don't want the design to have someone being massaged in it (pictures/photos) or have it look too clinical & sterile.

```html
<!DOCTYPE html>
<html lang="en">
<head>
<meta charset="utf-8">
<title>Tidal Touch &amp; Wellness – Business Card</title>
<link rel="stylesheet" href="https://fonts.googleapis.com/css2?family=Arimo&family=Archivo+Narrow:wght@500&family=Tinos:ital,wght@1,700&display=swap">
<style>
  :root {
    --paper: #ffffff;
    --mist: #eef5fa;
    --wave-light: #bcdcef;
    --wave: #5fa6d6;
    --wave-deep: #2f78b8;
    --ink: #111111;
    --brand-grey: #4a4f55;
    --name-green: #1aa37a;
    --title-teal: #1d6a68;
    --aqua: #8fd0ea;
  }
  html, body {
    margin: 0;
    padding: 0;
    width: 1200px;
    height: 704px;
    overflow: hidden;
    background: var(--paper);
  }
  .card {
    position: relative;
    width: 1200px;
    height: 704px;
    background: var(--paper);
    font-family: "Arimo", Arial, sans-serif;
  }
  .hero-banner {
    position: absolute;
    left: 0;
    top: 0;
    width: 1200px;
    height: 342px;
    background:
      radial-gradient(ellipse 70% 22% at 55% 58%, rgba(95,166,214,0.55), rgba(188,220,239,0) 70%),
      radial-gradient(ellipse 30% 40% at 10% 40%, rgba(95,166,214,0.45), rgba(188,220,239,0) 70%),
      linear-gradient(180deg, var(--mist) 0%, #f7fbfd 60%, var(--mist) 100%);
  }
  .hero-brand {
    position: absolute;
    left: 0;
    width: 1200px;
    top: 172px;
    text-align: center;
    font-size: 31px;
    color: var(--brand-grey);
    letter-spacing: 0.3px;
  }
  .brand-square {
    position: absolute;
    left: 137px;
    top: 349px;
    width: 68px;
    height: 68px;
    background: var(--aqua);
  }
  .details {
    position: absolute;
    left: 100px;
    top: 428px;
  }
  .details .brand-line {
    font-size: 22px;
    color: var(--brand-grey);
    margin: 0 0 16px;
  }
  .details p {
    margin: 0 0 21px;
    font-size: 24px;
    color: var(--ink);
    line-height: 1;
  }
  .identity {
    position: absolute;
    left: 700px;
    width: 486px;
    top: 432px;
    text-align: center;
  }
  .identity .person {
    margin: 0;
    font-family: "Tinos", "Times New Roman", serif;
    font-style: italic;
    font-weight: 700;
    font-size: 66px;
    line-height: 1;
    color: var(--name-green);
    transform: scaleX(0.88);
  }
  .identity .role {
    margin: 6px 0 0;
    font-family: "Archivo Narrow", "Arial Narrow", sans-serif;
    font-weight: 500;
    font-size: 50px;
    line-height: 1;
    color: var(--title-teal);
  }
</style>
</head>
<body>
  <div class="card">
    <div class="hero-banner" role="img" aria-label="Flowing blue water splash across a pale sky-blue background"></div>
    <div class="hero-brand">Tidal Touch &amp; Wellness</div>

    <div class="brand-square"></div>
    <div class="details">
      <div class="brand-line">Tidal Touch &amp; Wellness</div>
      <p>Swedish, Relaxation, Pregnancy.</p>
      <p>Deep Tissue &amp; Sports Massage</p>
      <p>Mobile: 0481 562 930</p>
      <p>E-mail: tidaltw@mailvane.com</p>
    </div>

    <div class="identity">
      <h1 class="person">Elise Brantry</h1>
      <h2 class="role">Massage Therapist</h2>
    </div>
  </div>
</body>
</html>
```